A5 flyer recto (just the front side) announcing the summer events

For a public aquarium in France, we invite you to create our A5 flyer recto (just the front side) announcing the events of this summer 2015
The flyer must be written in french, you will find attached all the text that you have to fill in the flyer.
You also have to use our logo in the top or in the bottom of the flyer (2 versions of the logo four color or black and white version. According your design you can use one of them)
We also have a mascot ( a sea horse), you can use it if you want to illustrate your design (attachment file)
We manage a mini-golf and we want to promote it with a special discount, you have to mentioned this benefit in the flyer as a special discount coupon)
You must specify our website and our adress..
We remain at your disposal for any question

```html
<!DOCTYPE html>
<html lang="fr">
<head>
<meta charset="utf-8">
<title>Aquarium des Brisants – Été 2015</title>
<link href="https://fonts.googleapis.com/css2?family=Signika:wght@400;600;700&family=PT+Sans:ital,wght@0,400;0,700;1,400;1,700&display=swap" rel="stylesheet">
<style>
  :root {
    --ocean-deep: #1b5fae;
    --ocean-mid: #3f8fd6;
    --ocean-light: #9fc9ee;
    --lagoon: #e6e4f4;
    --lagoon-soft: #f2f0fa;
    --ink: #283679;
    --tick: #d2232a;
    --coupon-green: #4c7a22;
    --footer: #2a4a8c;
    --white: #ffffff;
  }
  * { box-sizing: border-box; margin: 0; padding: 0; }
  html, body { width: 850px; height: 1200px; overflow: hidden; }
  body { font-family: "Signika", sans-serif; background: var(--lagoon); }
  .flyer {
    position: relative; width: 850px; height: 1200px; overflow: hidden;
    background: linear-gradient(180deg, var(--ocean-deep) 0%, var(--ocean-mid) 14%, var(--ocean-light) 26%, var(--lagoon) 36%, var(--lagoon-soft) 60%, var(--lagoon) 80%, #c9d6ee 100%);
  }
  .art { position: absolute; z-index: 1; }
  .art-dolphin { left: 10px; top: 105px; width: 500px; height: 250px; border-radius: 60% 50% 40% 60%; background: radial-gradient(ellipse at 60% 45%, #3e5fb8 0%, #2c4aa0 55%, rgba(44,74,160,0) 72%); }
  .art-diver-boy { left: 490px; top: 235px; width: 270px; height: 195px; border-radius: 45%; background: radial-gradient(ellipse at 45% 45%, #f0b08e 0%, #d24a5a 45%, rgba(210,74,90,0) 72%); }
  .art-clownfish { left: 655px; top: 145px; width: 145px; height: 75px; border-radius: 50%; background: radial-gradient(ellipse, #f26a22 0%, #f48a3a 55%, rgba(244,138,58,0) 72%); }
  .art-tang { left: 765px; top: 265px; width: 90px; height: 110px; border-radius: 50%; background: radial-gradient(ellipse, #3b4ea8 0%, #f2c63a 50%, rgba(242,198,58,0) 72%); }
  .art-seahorse { left: 15px; top: 345px; width: 230px; height: 575px; border-radius: 45% 55% 40% 50%; background: radial-gradient(ellipse at 50% 40%, #a9cf5a 0%, #8fbe46 50%, rgba(143,190,70,0) 72%); }
  .art-diver-girl { left: 0; top: 885px; width: 340px; height: 240px; border-radius: 50% 50% 30% 30%; background: radial-gradient(ellipse at 45% 45%, #f2b99a 0%, #d65aa8 45%, #e06a3a 60%, rgba(224,106,58,0) 74%); }

  .brand { position: absolute; left: 32px; top: 62px; z-index: 3; display: flex; align-items: center; gap: 10px; }
  .brand-dot { width: 22px; height: 22px; border-radius: 50%; background: var(--white); }
  .brand-name { font-weight: 700; font-size: 30px; line-height: 1.05; color: var(--white); }

  .info { position: absolute; right: 38px; top: 34px; z-index: 3; text-align: right; font-family: "PT Sans", sans-serif; color: var(--white); font-size: 17.5px; line-height: 24px; text-transform: uppercase; letter-spacing: .3px; }
  .info strong { display: block; text-transform: none; font-size: 18px; }

  .event { position: absolute; z-index: 3; color: var(--ink); font-size: 18.5px; line-height: 26.5px; text-transform: uppercase; text-align: justify; }
  .event b { font-weight: 700; }
  .event .tick { color: var(--tick); font-weight: 700; margin-right: 3px; }
  .event-touch { left: 172px; top: 362px; width: 350px; }
  .event-feeding { left: 258px; top: 437px; width: 555px; }
  .event-night { left: 256px; top: 510px; width: 557px; }
  .event-night .cast { display: block; margin-left: -42px; }
  .event-workshop { left: 158px; top: 685px; width: 655px; }
  .event-expo { left: 115px; top: 810px; width: 698px; }

  .cut-line { position: absolute; left: 0; top: 910px; width: 850px; border-top: 2px dotted #6b7bb0; z-index: 2; }
  .scissors { position: absolute; right: 48px; top: 898px; z-index: 3; }

  .coupon { position: absolute; left: 300px; top: 900px; width: 540px; z-index: 3; text-align: center; color: var(--coupon-green); text-transform: uppercase; }
  .coupon-title { display: inline-block; margin: 12px 0 30px; font-weight: 700; font-size: 34px; color: var(--coupon-green); }
  .coupon p { font-size: 18.5px; line-height: 26px; font-weight: 600; }
  .coupon p b { font-weight: 700; }
  .coupon .fine { margin-top: 10px; font-family: "PT Sans", sans-serif; font-style: italic; text-transform: none; font-size: 18px; font-weight: 400; }

  .footer { position: absolute; left: 0; bottom: 0; width: 850px; height: 78px; background: var(--footer); z-index: 2; color: var(--white); font-family: "PT Sans", sans-serif; font-size: 18.5px; line-height: 27px; text-align: center; padding: 10px 0 0 160px; }
</style>
</head>
<body>
<main class="flyer">
  <div class="art art-dolphin" role="img" aria-label="Illustration d'un dauphin bleu souriant"></div>
  <div class="art art-diver-boy" role="img" aria-label="Illustration d'un petit plongeur avec masque et palmes"></div>
  <div class="art art-clownfish" role="img" aria-label="Illustration d'un poisson-clown"></div>
  <div class="art art-tang" role="img" aria-label="Illustration d'un poisson tropical rayé"></div>
  <div class="art art-seahorse" role="img" aria-label="Illustration de la mascotte hippocampe verte"></div>
  <div class="art art-diver-girl" role="img" aria-label="Illustration d'une petite plongeuse entourée de poissons et de coraux"></div>

  <div class="brand">
    <span class="brand-dot"></span>
    <span class="brand-name">Aquarium<br>des Brisants</span>
  </div>

  <div class="info">
    Retrouvez toutes les informations,<br>
    tarif, horaires et conditions<br>
    d'inscriptions sur:
    <strong>aquariumdesbrisants.fr</strong>
  </div>

  <p class="event event-touch"><span class="tick">✓</span>Tous les jours, animations <b>« bassin tactile »</b> commentées</p>
  <p class="event event-feeding"><span class="tick">✓</span>Tous les après-midis nourrissages <b>commentés</b> de nos <b>espèces aquatiques.</b></p>
  <p class="event event-night"><span class="tick">✓</span>Les <b>mardis 21 &amp; 28 juillet, 4 &amp; 11 août</b> de <b>20h</b> à <b>23h</b>, les nocturnes de l'aquarium, avis de tempête découvrez l'aquarium des Brisants comme vous ne l'avez jamais visité.
    <span class="cast"><b>4 comédiens</b> investissent l'aquarium pour une visite drôle et décalée à faire en famille.</span></p>
  <p class="event event-workshop"><span class="tick">✓</span>Les <b>jeudis 9 &amp; 16 juillet, 20 &amp; 27 août</b> de <b>14h</b> à <b>17h</b>, pour les enfants de <b>6</b> à <b>12 ans</b>, l'aquarium propose des <b>ateliers scientifiques</b>. En compagnie d'un animateur, l'occasion d'apprendre en s'amusant.</p>
  <p class="event event-expo"><span class="tick">✓</span>En <b>juillet</b> &amp; <b>août</b>, exposition <b>« laisse de mer, source de vie »</b> de Maëlle Rivoal mieux comprendre la laisse de mer, son rôle écologique, son utilité pour nos plages...</p>

  <div class="cut-line"></div>
  <svg class="scissors" width="26" height="24" viewBox="0 0 26 24" aria-hidden="true">
    <circle cx="5" cy="6" r="4" fill="none" stroke="#283679" stroke-width="2"/>
    <circle cx="5" cy="18" r="4" fill="none" stroke="#283679" stroke-width="2"/>
    <path d="M8 8 L25 19 M8 16 L25 5" stroke="#283679" stroke-width="2"/>
  </svg>

  <section class="coupon">
    <span class="coupon-title">Mini-golf</span>
    <p>Sur présentation de ce <b>coupon</b>,<br>
    bénéficiez d'une partie mini-golf enfant<br>
    offerte pour une partie mini-golf adulte achetée *</p>
    <p class="fine">*offre non cumulable avec toute autre promotion</p>
  </section>

  <footer class="footer">
    Aquarium des Brisants, 14,<br>
    rue des Goélands, 56000 PORT-KERLANN, 02 98 00 12 34
  </footer>
</main>
</body>
</html>
```